Modern Business Card For A Digital Advertising Company

I'll be print on the Tarn Prints Velour paper http://us.tarnprints.example/products/velour/business-cards.html
Need's to be modern and use the color palette of the logo or gray scales. I think integrating the pixelation of the logo in to the card and having it wrap from one side to the other could be interesting. My company provides ad operations, web development, and number of other services to websites around the world. You can see my website at http://www.pixelharbor.example
Contact info on the card needs to have
Dana Welloby
President
p.555.318.4406
dana@pixelharbor.example
http://www.pixelharbor.example
Doesn't necessarily need to be in that order
Target Market(s)
Website owners
Industry/Entity Type
Business
Look and feel

```html
<!DOCTYPE html>
<html lang="en">
<head>
<meta charset="utf-8">
<title>Pixel Harbor – Business Card</title>
<link rel="stylesheet" href="https://fonts.googleapis.com/css2?family=Open+Sans:wght@400;600;700&display=swap">
<style>
  :root {
    --stage: #2d2d2d;
    --card: #ffffff;
    --brand-green: #8cc63f;
    --band-top: #8cc63f;
    --band-mid: #3f9a2c;
    --band-bottom: #0b6a22;
    --ink: #4a4a4a;
    --ink-dark: #222222;
    --divider: #d9f0b5;
  }
  * { box-sizing: border-box; margin: 0; padding: 0; }
  html, body {
    width: 1200px; height: 382px; overflow: hidden;
    background: var(--stage);
    font-family: "Open Sans", Arial, sans-serif;
  }
  .stage { position: relative; width: 1200px; height: 382px; }
  .card {
    position: absolute; top: 31px;
    width: 549px; height: 312px;
    background: var(--card);
    border-radius: 14px;
    overflow: hidden;
  }
  .card--front { left: 27px; }
  .card--back { left: 610px; border-radius: 14px 14px 2px 2px; }

  .wordmark {
    position: absolute;
    display: flex; align-items: center;
    color: var(--brand-green);
    font-weight: 700;
    white-space: nowrap;
  }
  .wordmark__square { background: var(--brand-green); flex: none; }

  .card--front .wordmark {
    left: 0; right: 0; top: 126px;
    justify-content: center; gap: 14px;
    font-size: 44px;
  }
  .card--front .wordmark__square { width: 36px; height: 36px; }

  .card--back .wordmark {
    left: 49px; top: 112px; gap: 10px;
    font-size: 28px;
  }
  .card--back .wordmark__square { width: 24px; height: 24px; }

  .holder {
    position: absolute; right: 34px; top: 26px;
    text-align: right; color: var(--ink);
  }
  .holder__name { font-size: 19px; font-weight: 700; line-height: 1.2; }
  .holder__title { font-size: 14px; color: var(--ink-dark); line-height: 1.3; }

  .contact-band {
    position: absolute; left: 0; right: 0; bottom: 0;
    height: 79px;
    background: linear-gradient(to bottom, var(--band-top) 0%, var(--band-mid) 45%, var(--band-bottom) 100%);
    display: flex; align-items: center;
    color: #ffffff; font-size: 14.5px;
  }
  .contact-band__item {
    height: 100%;
    display: flex; align-items: center; justify-content: center;
    white-space: nowrap;
  }
  .contact-band__item--phone { width: 143px; }
  .contact-band__item--email { width: 206px; }
  .contact-band__item--web { flex: 1; }
  .contact-band__divider {
    width: 3px; height: 68px; align-self: flex-end; margin-bottom: 3px;
    background: var(--divider); flex: none; border-radius: 1px;
  }
</style>
</head>
<body>
  <main class="stage">
    <section class="card card--front" aria-label="Card front">
      <div class="wordmark"><span class="wordmark__square"></span>Pixel Harbor</div>
    </section>

    <section class="card card--back" aria-label="Card back">
      <div class="wordmark"><span class="wordmark__square"></span>Pixel Harbor</div>
      <div class="holder">
        <p class="holder__name">Dana Welloby</p>
        <p class="holder__title">President</p>
      </div>
      <div class="contact-band">
        <span class="contact-band__item contact-band__item--phone">555-318-4406</span>
        <span class="contact-band__divider"></span>
        <span class="contact-band__item contact-band__item--email">dana@pixelharbor.example</span>
        <span class="contact-band__divider"></span>
        <span class="contact-band__item contact-band__item--web">www.pixelharbor.example</span>
      </div>
    </section>
  </main>
</body>
</html>
```